Graphic Design Project

i need Demo graphics designed for my Restaurant App. The app name "TablePeek Plus".
This a Demo app to show potential restaurant owners to try to get them to buy. With the app you can view restaurant men us, specials and events. Post Fanwall and reviews. Alot of other options.
I need the main screen and icons created with the TablePeek Plus logo created. I also need the Specials page created that i will use for the events page also. Also need the reviews page created that i will use for the fanwall page also.
I also need a menu page designed and to match the theme.
I uploaded a few sample screenshots of the current app design.
Updates

Payment is now Guarantee.

Project Deadline Extended
Reason: Need more time for submissions

Hi Do you plan on submitting an updated design soon?

Target Market(s)

restaurant owners. trying to sell them the app.

Industry/Entity Type

Restaurant

Requirements
Must have
• background of something nice that represent a a restaurant but not specific to any one type pf food. Maybe like spoon and fork design or something.
Nice to have
• different icons that represent the different buttons.
eye catching design.
ease of use buttons.

```html
<!DOCTYPE html>
<html lang="en">
<head>
<meta charset="utf-8">
<title>TablePeek Plus – App Screens</title>
<link rel="stylesheet" href="https://fonts.googleapis.com/css2?family=Arimo:wght@400;700&family=Bitter:wght@700;800&family=Montserrat:wght@500;700&family=Questrial&display=swap">
<style>
  :root{
    --page:#ffffff;
    --status:#000000;
    --nav-top:#3a3a3a;
    --nav-bottom:#0c0c0c;
    --red:#c8161d;
    --deep-red:#8a0f12;
    --gold-light:#f3dcae;
    --gold:#c9933f;
    --gold-dark:#6a4412;
    --cream:#f6ecd2;
    --cork:#b58a5c;
    --parchment:#efdcab;
    --parchment-edge:#b0884a;
    --ink:#141414;
    --paper-light:#f2ede5;
  }
  *{box-sizing:border-box;margin:0;padding:0}
  html,body{width:1200px;height:900px;overflow:hidden;background:var(--page)}
  .stage{position:relative;width:1200px;height:900px}
  .screen{position:absolute;top:236px;width:285px;height:428px;overflow:hidden;background:#000;font-family:"Arimo",sans-serif}
  .screen--home{left:10px}
  .screen--specials{left:305px}
  .screen--menu{left:605px}
  .screen--fanwall{left:905px}

  .status-bar{position:absolute;top:0;left:0;right:0;height:20px;background:var(--status);color:#fff;font-size:11.5px;display:flex;align-items:center;padding:0 6px}
  .status-bar .carrier{flex:1;display:flex;align-items:center;gap:4px}
  .status-bar .clock{font-weight:700;font-size:12.5px}
  .status-bar .battery{flex:1;display:flex;justify-content:flex-end;align-items:center;gap:4px}

  .nav-bar{position:absolute;top:20px;left:0;right:0;height:34px;background:linear-gradient(var(--nav-top),var(--nav-bottom));color:#fff;display:flex;align-items:center;justify-content:center;font-weight:700;font-size:16px;border-bottom:1px solid #000}
  .nav-button{position:absolute;top:6px;height:22px;padding:0 8px;border-radius:4px;background:linear-gradient(#4a4a4a,#1a1a1a);border:1px solid #000;font-size:10.5px;display:flex;align-items:center}
  .nav-button--left{left:6px;padding-left:12px;clip-path:polygon(8px 0,100% 0,100% 100%,8px 100%,0 50%)}
  .nav-button--right{right:6px}

  /* Home */
  .home-backdrop{position:absolute;top:20px;left:0;right:0;bottom:0;background:
    radial-gradient(circle at 20% 85%,rgba(230,170,80,.55),transparent 35%),
    radial-gradient(circle at 80% 70%,rgba(220,150,60,.5),transparent 40%),
    linear-gradient(#0a0a0a 0%,#2b2b2e 35%,#3a2c1a 60%,#5b3f1c 100%)}
  .brand-title{position:absolute;left:0;right:0;text-align:center;font-family:"Bitter",serif;font-weight:800;color:var(--cream)}
  .home-brand{top:66px;font-size:25px;line-height:1.05}
  .home-brand .dot{display:block;width:34px;height:34px;border-radius:50%;background:var(--red);margin:0 auto 8px}
  .menu-grid{position:absolute;top:158px;left:12px;right:8px;display:grid;grid-template-columns:130px 130px;column-gap:10px;row-gap:13px}
  .menu-tile{height:34px;border-radius:16px 4px 16px 4px;background:linear-gradient(160deg,var(--gold-light) 0%,var(--gold) 45%,var(--gold-dark) 100%);display:flex;align-items:center;justify-content:center;font-family:"Bitter",serif;font-weight:800;font-size:16px;color:var(--cream);text-shadow:0 1px 2px #3a2200;box-shadow:0 2px 3px rgba(0,0,0,.6)}
  .menu-tile--light{background:linear-gradient(160deg,#fff4dc 0%,var(--gold-light) 40%,#b78b4a 100%)}
  .footer-mark{position:absolute;bottom:6px;left:0;right:0;text-align:center;font-family:"Bitter",serif;font-weight:800;font-size:9px;color:var(--red)}

  /* Specials */
  .cork-board{position:absolute;top:54px;left:14px;right:14px;bottom:0;background:radial-gradient(circle,#c9a274,var(--cork))}
  .day-heading{position:absolute;left:0;right:0;text-align:center;font-family:"Bitter",serif;font-weight:800;font-size:23px;color:var(--red);text-shadow:0 1px 0 #fff}
  .special-card{position:absolute;left:8px;right:8px;background:var(--paper-light);border:1px solid #8b6a45;box-shadow:1px 2px 3px rgba(0,0,0,.5);padding:5px 6px;font-size:7.5px;line-height:1.3;color:var(--ink)}
  .special-card strong{color:var(--deep-red);display:block}

  /* Menu */
  .parchment{position:absolute;top:54px;left:14px;right:14px;bottom:0;background:radial-gradient(ellipse at 50% 40%,#f7e8c2,var(--parchment) 60%,var(--parchment-edge));box-shadow:0 0 0 3px #2a1a08}
  .section-title{position:absolute;top:16px;left:0;right:0;text-align:center;font-family:"Bitter",serif;font-weight:800;font-size:26px;color:var(--red)}
  .section-band{position:absolute;top:58px;left:40px;right:40px;height:32px;background:linear-gradient(90deg,transparent,var(--red) 15%,var(--red) 85%,transparent);color:#fff;font-size:8.5px;text-align:center;line-height:1.2;padding-top:5px;font-family:"Questrial",sans-serif}
  .dish{position:absolute;left:14px;right:14px;font-family:"Montserrat",sans-serif}
  .dish-head{display:flex;justify-content:space-between;font-weight:700;font-size:15.5px;color:var(--ink)}
  .dish-desc{font-style:italic;font-size:9.5px;text-align:center;line-height:1.2;margin-top:6px;color:var(--ink)}

  /* Fanwall */
  .fanwall-paper{position:absolute;top:54px;left:14px;right:14px;bottom:0;background:radial-gradient(ellipse,#f8f4ee,#e3d8c6)}
  .fanwall-brand{top:18px;font-size:20px;color:#d9ccb3;line-height:1.1}
  .fanwall-brand .dot{display:block;width:40px;height:40px;border-radius:50%;background:var(--red);margin:0 auto 8px}
  .post{position:absolute;left:24px;right:24px;padding-bottom:10px;border-bottom:2px solid var(--deep-red)}
  .post-author{font-weight:700;font-size:17px;color:var(--ink)}
  .post-date{font-size:9px;margin-top:2px}
  .post-body{font-size:15px;margin-top:3px}
</style>
</head>
<body>
<main class="stage">

  <!-- Home screen -->
  <section class="screen screen--home">
    <div class="home-backdrop" role="img" aria-label="Night city skyline with warm golden bokeh lights"></div>
    <div class="status-bar"><span class="carrier">NetCo ︎</span><span class="clock">10:26 AM</span><span class="battery">85%
      <svg width="20" height="10" viewBox="0 0 20 10"><rect x=".5" y=".5" width="17" height="9" rx="1.5" fill="none" stroke="#fff"/><rect x="2" y="2" width="13" height="6" fill="#fff"/><rect x="18" y="3" width="2" height="4" fill="#fff"/></svg></span></div>
    <div class="brand-title home-brand"><span class="dot"></span>TablePeek Plus</div>
    <nav class="menu-grid">
      <div class="menu-tile menu-tile--light">Menu</div><div class="menu-tile">Specials</div>
      <div class="menu-tile">Directions</div><div class="menu-tile">Rewiews</div>
      <div class="menu-tile">Gallery</div><div class="menu-tile">Friendbook</div>
      <div class="menu-tile">Fanwall</div><div class="menu-tile">Pools</div>
      <div class="menu-tile">Events</div><div class="menu-tile menu-tile--light">More</div>
    </nav>
    <div class="footer-mark">TablePeek Plus</div>
  </section>

  <!-- Specials screen -->
  <section class="screen screen--specials">
    <div class="status-bar"><span class="carrier">NetCo</span><span class="clock">8:34 AM</span><span class="battery">17%
      <svg width="20" height="10" viewBox="0 0 20 10"><rect x=".5" y=".5" width="17" height="9" rx="1.5" fill="none" stroke="#fff"/><rect x="2" y="2" width="3" height="6" fill="#fff"/><rect x="18" y="3" width="2" height="4" fill="#fff"/></svg></span></div>
    <header class="nav-bar"><span class="nav-button nav-button--left">Back</span>Specials</header>
    <div class="cork-board" role="img" aria-label="Cork board texture">
      <h2 class="day-heading" style="top:12px">Monday</h2>
      <div class="special-card" style="top:42px;height:72px"><strong>ALL DAY HAPPYHOUR</strong>.45¢ wings</div>
      <h2 class="day-heading" style="top:124px">Wednesday</h2>
      <div class="special-card" style="top:154px;height:78px"><strong>KIDS NIGHT</strong>Kids under 12 eat free from kids menu when accompanied by an adult,all day Compimentary face Painting 5:30-8:30 <span style="color:var(--deep-red)">Karaoke Night</span> begins @ 10:00PM - Must be 21 or order</div>
      <h2 class="day-heading" style="top:240px">Friday</h2>
      <div class="special-card" style="top:270px;height:48px"><strong>FISH FRY W/SPAGHETTI</strong>All you can eat!</div>
      <div class="footer-mark">TablePeek Plus</div>
    </div>
  </section>

  <!-- Menu screen -->
  <section class="screen screen--menu">
    <div class="status-bar"><span class="carrier">NetCo</span><span class="clock">8:54 AM</span><span class="battery">35%
      <svg width="20" height="10" viewBox="0 0 20 10"><rect x=".5" y=".5" width="17" height="9" rx="1.5" fill="none" stroke="#fff"/><rect x="2" y="2" width="5" height="6" fill="#fff"/><rect x="18" y="3" width="2" height="4" fill="#fff"/></svg></span></div>
    <header class="nav-bar"><span class="nav-button nav-button--left">Dinner</span>Appetizers</header>
    <div class="parchment">
      <h2 class="section-title">Appetizers</h2>
      <div class="section-band">SOMETHING FOR STARTERS<br>OR DELICIOUS AS A MEAL</div>
      <div class="dish" style="top:106px"><div class="dish-head"><span>MINI Burgers</span><span>$5.95</span></div>
        <p class="dish-desc">Mini burgers with seasoned peppers and onions, mushrooms, lettuce, tomato, dipped in BBQ sauce and topped with Swiss cheese on a House Roll. Served with seasoned fries.</p></div>
      <div class="dish" style="top:214px"><div class="dish-head"><span>Chicken Salad</span><span>$4.00</span></div>
        <p class="dish-desc">Chicken salad with lettuce and tomato on a House Roll. Served with seasoned fries and fresh fruit garnish.</p></div>
      <div class="dish" style="top:298px"><div class="dish-head"><span>Wing Dings</span><span>$6.75</span></div></div>
      <div class="footer-mark">TablePeek Plus</div>
    </div>
  </section>

  <!-- Fanwall screen -->
  <section class="screen screen--fanwall">
    <div class="status-bar"><span class="carrier">NetCo</span><span class="clock">8:34 AM</span><span class="battery">16%
      <svg width="20" height="10" viewBox="0 0 20 10"><rect x=".5" y=".5" width="17" height="9" rx="1.5" fill="none" stroke="#fff"/><rect x="2" y="2" width="3" height="6" fill="#fff"/><rect x="18" y="3" width="2" height="4" fill="#fff"/></svg></span></div>
    <header class="nav-bar"><span class="nav-button nav-button--left">Back</span>Fanwall<span class="nav-button nav-button--right">Post</span></header>
    <div class="fanwall-paper">
      <div class="brand-title fanwall-brand"><span class="dot"></span>TablePeek Plus</div>
      <article class="post" style="top:120px"><div class="post-author">Tony</div><div class="post-date">2012-04-14 09:30:59</div><div class="post-body">Great app</div></article>
      <article class="post" style="top:194px"><div class="post-author">Josh</div><div class="post-date">2011-08-15 11:04:56</div><div class="post-body">Awsome salads</div></article>
      <div class="footer-mark">TablePeek Plus</div>
    </div>
  </section>

</main>
</body>
</html>
```